Tallyleaf Web Design

Create Website Design for Tallyleaf. Tallyleaf is online application for collaboration team work system (task list management). More concept design for this project please find attach file ("tallyleaf website concept.pdf") . But my concept is just describe minimal features not bind design

For tallyleaf logo, i had already attach files. But i had not decided what color i chose, so it's okay if you suggest logo color for your suitable website design.
Updates

Dear All Designer,

I like brisk carousel (http://quorvanlabs.example/brisk-carousel/),
may be your concept design can adjust with this concept.
but don't worry about script for brisk carousel, my team will be handle
You just make website design to suitable with brisk carousel

but if you had own website design concept are welcome

thanks

Target Market(s)

Business Company

Industry/Entity Type

Management

```html
<!DOCTYPE html>
<html lang="en">
<head>
<meta charset="utf-8">
<title>Tallyleaf</title>
<link href="https://fonts.googleapis.com/css2?family=Ubuntu:wght@400;500;700&family=Open+Sans:wght@400;600&display=swap" rel="stylesheet">
<style>
:root{
  --teal-dark:#1f4a59;
  --teal-line:#2b6a86;
  --panel:#2f6482;
  --green:#7db83a;
  --welcome-ink:#2f4a10;
  --grey-band:#ececec;
  --card-border:#dcdcdc;
  --text:#333;
  --orange:#d9820b;
  --orange-line:#c27208;
  --footer-text:#fff4e0;
  --black:#111;
  --badge-blue:#1aa0d8;
  --badge-green:#1fae6a;
}
*{box-sizing:border-box;margin:0;padding:0}
html,body{width:1200px;height:1095px;overflow:hidden}
body{position:relative;font-family:"Open Sans",Arial,sans-serif;background:#fff;color:var(--text)}

.site-header{position:absolute;left:0;top:0;width:1200px;height:106px;background:linear-gradient(#fff,#f3f3f3);border-bottom:4px solid var(--teal-line)}
.brand{position:absolute;left:86px;top:26px;display:flex;align-items:center;gap:10px}
.brand-name{font-family:"Ubuntu",sans-serif;font-weight:500;font-size:46px;color:var(--teal-dark);letter-spacing:-0.5px}
.brand-dot{width:20px;height:20px;border-radius:50%;background:var(--green)}

.account-tab{position:absolute;left:948px;top:0;width:168px;height:28px;background:var(--teal-dark);display:flex;justify-content:space-around;align-items:center;font-family:"Ubuntu",sans-serif;font-size:13px;color:#fff;border-radius:0 0 3px 3px}
.account-tab span{display:flex;align-items:center;gap:6px}
.account-tab svg{width:12px;height:12px}

.main-nav{position:absolute;left:567px;top:46px;display:flex;font-family:"Ubuntu",sans-serif;font-weight:500;font-size:21px;color:var(--teal-dark)}
.main-nav a{color:inherit;text-decoration:none;padding:4px 11px;height:36px;display:block;position:relative}
.main-nav a.is-active{background:var(--teal-dark);color:#fff;border-radius:2px}
.main-nav a.is-active::after{content:"";position:absolute;left:62px;bottom:-8px;border:8px solid transparent;border-top-color:var(--teal-dark);border-bottom:0}

.hero{position:absolute;left:0;top:110px;width:1200px;height:504px}
.hero-photo{position:absolute;inset:0;background:
  radial-gradient(ellipse at 40% 85%,#6c9a3a 0%,rgba(108,154,58,0) 45%),
  radial-gradient(ellipse at 75% 70%,#d9905a 0%,rgba(217,144,90,0) 30%),
  radial-gradient(ellipse at 20% 20%,#c9d3c9 0%,rgba(201,211,201,0) 40%),
  linear-gradient(160deg,#8ea08e 0%,#4f6a45 45%,#3c5a2c 70%,#b7c4b0 100%)}
.welcome-art{position:absolute;left:137px;top:44px;width:394px;height:394px;border-radius:50%;background:radial-gradient(circle at 42% 38%,#b7dc3c 0%,#8cc021 55%,#6ea516 100%)}
.welcome-text{position:absolute;left:134px;top:150px;width:400px;text-align:center;font-family:"Ubuntu",sans-serif;font-weight:700;font-size:56px;line-height:62px;color:var(--welcome-ink)}

.signup-panel{position:absolute;left:764px;top:108px;width:352px;height:454px;background:var(--panel);background-image:repeating-linear-gradient(45deg,rgba(255,255,255,.03) 0 2px,transparent 2px 5px);border-radius:0 0 4px 4px}
.email-field{position:absolute;left:24px;top:56px;width:299px;height:38px;background:#fff;border:1px solid #c9c9c9;font-size:15px;color:#9a9a9a;padding:9px 10px}
.btn-start{position:absolute;left:24px;top:111px;width:299px;height:42px;background:linear-gradient(#92c94a,#5d9a22);border:1px solid #4c7e1a;color:#fff;font-family:"Ubuntu",sans-serif;font-weight:500;font-size:18px;text-align:center;line-height:40px}
.or{position:absolute;left:0;top:160px;width:352px;text-align:center;color:#fff;font-size:16px}
.btn-alt{position:absolute;left:24px;top:195px;width:299px;height:40px;background:linear-gradient(#f4f4f4,#cfcfcf);border:1px solid #aaa;color:#555;font-size:17px;text-align:center;line-height:38px}
.badge{position:absolute;top:270px;width:130px;height:130px;border-radius:50%}
.badge-blue{left:44px;background:var(--badge-blue)}
.badge-green{left:180px;background:var(--badge-green)}

.features{position:absolute;left:0;top:614px;width:1200px;height:234px;background:var(--grey-band)}
.feature-card{position:absolute;top:27px;width:286px;height:175px;background:#fff;border:1px solid var(--card-border);box-shadow:0 1px 2px rgba(0,0,0,.12)}
.feature-card:nth-child(1){left:84px}
.feature-card:nth-child(2){left:453px}
.feature-card:nth-child(3){left:830px}
.feature-media{height:99px;background:linear-gradient(100deg,#d6eef7 0%,#6ec2e4 40%,#ffffff 70%,#9fb2c7 100%)}
.feature-title{position:absolute;left:14px;top:5px;font-family:"Ubuntu",sans-serif;font-weight:700;font-size:20px;color:#1d3440;white-space:nowrap}
.feature-card p{padding:8px 12px;font-size:12.5px;line-height:20px;color:#444}
.device-icons{position:absolute;left:45px;top:28px}
.feature-card.sync .feature-title{top:3px;font-weight:500;font-size:21px}
.feature-card.sync p{position:absolute;top:99px}

.site-footer{position:absolute;left:0;top:848px;width:1200px;height:211px;background:var(--orange)}
.footer-col{position:absolute;top:30px;color:var(--footer-text)}
.footer-col h3{font-family:"Ubuntu",sans-serif;font-weight:400;font-size:18px;color:#fff;margin-bottom:10px}
.footer-col p{font-size:12.5px;line-height:21px;width:300px}
.footer-col ul{list-style:none}
.footer-col li{font-size:13px;line-height:21px;padding-left:20px;position:relative}
.footer-col li::before{content:"";position:absolute;left:2px;top:10px;width:9px;height:1px;background:#fff}
.footer-col li::after{content:"";position:absolute;left:8px;top:8px;border:2.5px solid transparent;border-left:4px solid #fff}
.divider{position:absolute;top:28px;width:1px;height:160px;background:var(--orange-line)}
.bottom-bar{position:absolute;left:0;top:1059px;width:1200px;height:36px;background:var(--black);color:#ddd;font-size:12px;line-height:36px;padding-left:84px}
</style>
</head>
<body>

<header class="site-header">
  <div class="brand"><span class="brand-name">tallyleaf</span><span class="brand-dot"></span></div>
  <div class="account-tab">
    <span><svg viewBox="0 0 12 12"><circle cx="6" cy="3.5" r="3" fill="#fff"/><path d="M0 12c0-4 3-5.5 6-5.5s6 1.5 6 5.5z" fill="#fff"/></svg>Login</span>
    <span><svg viewBox="0 0 12 12"><circle cx="6" cy="3.5" r="3" fill="#fff"/><path d="M0 12c0-4 3-5.5 6-5.5s6 1.5 6 5.5z" fill="#fff"/></svg>Register</span>
  </div>
  <nav class="main-nav">
    <a class="is-active" href="#">Home</a>
    <a href="#">About</a>
    <a href="#">Tour</a>
    <a href="#">Pricing</a>
    <a href="#">Free Trial</a>
    <a href="#">Customers</a>
  </nav>
</header>

<section class="hero">
  <div class="hero-photo" role="img" aria-label="Blurred photo of a fresh produce market stall with green vegetables"></div>
  <div class="welcome-art" role="img" aria-label="Glossy green speech bubble illustration"></div>
  <div class="welcome-text">Welcome to the Tallyleaf</div>
</section>

<aside class="signup-panel">
  <div class="email-field">Your email</div>
  <div class="btn-start">GET STARTED</div>
  <div class="or">or</div>
  <div class="btn-alt">Sign in with Gloopin</div>
  <div class="badge badge-blue" role="img" aria-label="Press award badge"></div>
  <div class="badge badge-green" role="img" aria-label="Industry listing badge"></div>
</aside>

<section class="features">
  <article class="feature-card">
    <div class="feature-media" role="img" aria-label="Puzzle pieces illustration on a blue swirl"></div>
    <h2 class="feature-title">Customize application</h2>
    <p>That it has a more-or-less normal distribution of letters, as opposed to using.</p>
  </article>
  <article class="feature-card">
    <div class="feature-media" role="img" aria-label="Puzzle pieces illustration on a blue swirl"></div>
    <h2 class="feature-title">Customize application</h2>
    <p>Lorem Ipsum is that it has a more-or-less normallike readable English.</p>
  </article>
  <article class="feature-card sync">
    <h2 class="feature-title">Synchronize all device</h2>
    <svg class="device-icons" width="200" height="68" viewBox="0 0 200 68">
      <rect x="4" y="30" width="22" height="34" rx="3" fill="none" stroke="#444" stroke-width="4"/>
      <rect x="48" y="18" width="56" height="46" rx="5" fill="none" stroke="#444" stroke-width="5"/>
      <rect x="128" y="4" width="66" height="46" rx="2" fill="none" stroke="#444" stroke-width="5"/>
      <path d="M155 50 L151 62 H171 L167 50" fill="#444"/>
    </svg>
    <p>Lorem Ipsum is that it has a more-or-less normal English.</p>
  </article>
</section>

<footer class="site-footer">
  <div class="footer-col" style="left:86px">
    <h3>Ask Us A Question</h3>
    <p>Lorem Ipsum is that it has a more-or-less normal distribution of letters, as opposed to using 'Content here, content here', making it look like readable English.</p>
  </div>
  <div class="divider" style="left:418px"></div>
  <div class="footer-col" style="left:456px">
    <h3>Site Map</h3>
    <ul><li>Home</li><li>About Us</li><li>Music Tours</li><li>Music Festivals</li></ul>
  </div>
  <div class="divider" style="left:598px"></div>
  <div class="footer-col" style="left:624px">
    <h3>Music Tours</h3>
    <ul><li>Shanghai</li><li>Sydney</li><li>Beijing</li><li>Brisbane</li></ul>
  </div>
  <div class="divider" style="left:780px"></div>
  <div class="footer-col" style="left:802px">
    <h3>Sports Tours</h3>
    <ul><li>Havana</li><li>Honolulu</li><li>Sydney</li><li>Beijing</li></ul>
  </div>
  <div class="divider" style="left:958px"></div>
  <div class="footer-col" style="left:1003px">
    <h3>Other Tours</h3>
    <ul><li>Honolulu</li><li>Shanghai</li><li>Brisbane</li><li>Sydney</li></ul>
  </div>
</footer>
<div class="bottom-bar">Copyright © 2013 Meridian Works Pacific.</div>

</body>
</html>
```